Web App Dashboard Design for Healthcare Company

We have developed a simple web application with 3 navigation menus. We like the current design (very much modeled after Ledgerly), but we want to explore UI options for the branding, header, menus, and footer that we may not have considered.

The attached screenshots show the layout and two menu "hover" views as they currently exist.

This web application is used by employees only.

Menu 1 - Module Menu:
Allows the user to switch easily between Account, Employee, and Care Management.

Menu 2 - Reports Menu
Allows user to view available reports within each Module.

Menu 3 - Admin Menu
Allows the user to easily create new content types within each module.

Use our branded colors and font.

Colors:
Logo Blue (dark): 00c0f3
Logo Blue (light): 44c8f5
Nav Blue: 0994d0
Green: 71b44b
Grayscale: (not specified)

Font:
Lato (Google Font)

Target Market(s)

Internal staff.

Industry/Entity Type

Healthcare

Number of Pages Required

3 page

Font styles to use
Sans Serif
Other font styles liked:
• Lato (Google Font)

Colors
0293ce
9bcb3c

Requirements
Must have
• It's really a one page design, but we want to see the two "hover" views for the Module Menu and the Admin Menu.
• It should also be very clear which "Report" page the user is on (the active menu link).
• Must use branded colors, font, and logo.
• Logo Blue (dark): 00c0f3
• Logo Blue (light): 44c8f5
• Nav Blue: 0994d0
• Green: 71b44b
• Grayscale: Designer may choose
Nice to have
• It would be nice to have simple uncluttered payouts.
Should not have
• The design should not have menu options exposed by default.

```html
<!DOCTYPE html>
<html lang="en">
<head>
<meta charset="utf-8">
<title>CareLoop – Reminders</title>
<link rel="stylesheet" href="https://fonts.googleapis.com/css2?family=Lato:wght@400;700&display=swap">
<style>
  :root {
    --header-bg: #ffffff;
    --page-bg: #d5e9f2;
    --page-bg-light: #eaf4f8;
    --side-top: #2e2e2e;
    --side-bottom: #222222;
    --side-footer: #333333;
    --nav-active: #36a5d8;
    --table-head: #37a3d6;
    --row-odd: #f1f6f8;
    --row-even: #e9eff2;
    --cell-line: #d7e0e4;
    --text: #3a3a3a;
    --text-light: #ffffff;
    --badge-red: #ff3b3b;
    --badge-green: #6cb24c;
    --link: #1f43d8;
    --brand-blue: #00c0f3;
    --brand-green: #71b44b;
    --user-name: #2b3a42;
    --user-role: #8a8f93;
    --dot-orange: #f7941d;
    --dot-red: #e8212b;
  }
  * { box-sizing: border-box; margin: 0; padding: 0; }
  html, body { width: 1200px; height: 651px; overflow: hidden; }
  body {
    font-family: "Lato", sans-serif;
    color: var(--text);
    position: relative;
    background: linear-gradient(160deg, var(--page-bg-light), var(--page-bg) 60%, #e3eff4);
  }

  /* Header */
  .app-header {
    position: absolute; left: 0; top: 0; width: 1200px; height: 69px;
    background: var(--header-bg);
  }
  .brand {
    position: absolute; left: 48px; top: 20px;
    display: flex; align-items: center; gap: 8px;
    font-size: 22px; font-weight: 700; color: var(--brand-blue);
  }
  .brand-mark { width: 20px; height: 20px; background: var(--brand-green); border-radius: 50%; }
  .header-tools { position: absolute; top: 22px; left: 0; }
  .tool { position: absolute; top: 0; width: 22px; height: 22px; }
  .tool svg { display: block; }
  .tool .count {
    position: absolute; right: -3px; top: -4px; width: 10px; height: 10px; border-radius: 50%;
    font-size: 7px; line-height: 10px; text-align: center; color: #fff;
  }
  .header-divider { position: absolute; left: 1035px; top: 10px; width: 1px; height: 48px; background: #e2e2e2; }
  .avatar { position: absolute; left: 1055px; top: 18px; width: 31px; height: 31px; border-radius: 50%;
    background: radial-gradient(circle at 50% 40%, #c99a7e, #4a2b1e); }
  .user { position: absolute; left: 1095px; top: 17px; }
  .user-name { font-size: 15.5px; font-weight: 700; color: var(--user-name); line-height: 18px; }
  .user-role { font-size: 11px; color: var(--user-role); line-height: 16px; }

  /* Sidebar */
  .sidebar { position: absolute; left: 0; top: 84px; width: 223px; height: 567px; background: var(--side-bottom); }
  .search {
    height: 54px; background: var(--side-top); padding: 16px 19px 0;
  }
  .search-field {
    display: flex; justify-content: space-between; align-items: center;
    border-bottom: 1px solid #8c8c8c; height: 24px; color: #eee; font-size: 13px;
  }
  .nav-group { list-style: none; }
  .nav-group.modules { background: var(--side-top); padding-bottom: 20px; }
  .nav-group.admin { padding-top: 4px; }
  .nav-item {
    position: relative; height: 51.4px; display: flex; align-items: center;
    padding-left: 22px; gap: 9px; color: var(--text-light); font-size: 13px; font-weight: 700;
  }
  .nav-item.active { background: var(--nav-active); height: 43px; }
  .nav-item.active::after {
    content: ""; position: absolute; right: 0; top: 15px;
    border: 6px solid transparent; border-right-color: var(--page-bg-light);
  }
  .nav-icon {
    width: 29px; height: 29px; border-radius: 50%; background: #fff;
    display: flex; align-items: center; justify-content: center; flex: none;
  }
  .nav-item.active .nav-icon { background: #2b2b2b; }
  .sidebar-footer {
    position: absolute; left: 0; bottom: 0; width: 223px; height: 54px;
    background: var(--side-footer); color: #f0f0f0; font-size: 11px; line-height: 17px;
    text-align: center; padding-top: 10px;
  }

  /* Table */
  .reminders {
    position: absolute; left: 243px; top: 85px; width: 936px;
    border-collapse: collapse; table-layout: fixed; font-size: 12px;
  }
  .reminders th {
    background: var(--table-head); color: var(--text-light); height: 51px;
    font-size: 14.5px; font-weight: 700; text-align: left; padding-left: 15px;
    border-right: 1px solid #5fb7e0; white-space: nowrap;
  }
  .reminders th:last-child { border-right: 0; }
  .reminders td {
    height: 51.4px; padding-left: 17px; border-right: 1px solid var(--cell-line); white-space: nowrap;
  }
  .reminders td:last-child { border-right: 0; padding-left: 23px; }
  .reminders tbody tr:nth-child(odd) { background: var(--row-odd); }
  .reminders tbody tr:nth-child(even) { background: var(--row-even); }
  .sort-caret { display: inline-block; margin-left: 5px; border: 4.5px solid transparent; border-top-color: #fff; vertical-align: -2px; }
  .status {
    display: inline-block; width: 103px; height: 17px; line-height: 17px; text-align: center;
    color: #fff; font-size: 12px;
  }
  .status.overdue { background: var(--badge-red); }
  .status.done { background: var(--badge-green); }
  .row-link { color: var(--link); text-decoration: none; }

  /* Pagination */
  .pager { position: absolute; left: 617px; top: 585px; display: flex; align-items: center; font-size: 12px; color: #222; }
  .pager-arrow { width: 23px; height: 23px; }
  .pager-pages { display: flex; gap: 13px; margin: 0 15px 0 14px; }
  .pager-pages .current { font-weight: 700; }
</style>
</head>
<body>
  <header class="app-header">
    <div class="brand"><span class="brand-mark"></span>CareLoop</div>

    <div class="header-tools">
      <span class="tool" style="left:856px">
        <svg width="20" height="20" viewBox="0 0 20 20"><circle cx="10" cy="10" r="10" fill="#111"/><rect x="8.6" y="4" width="2.8" height="8" rx="1" fill="#fff"/><circle cx="10" cy="15" r="1.5" fill="#fff"/></svg>
      </span>
      <span class="tool" style="left:893px">
        <svg width="16" height="18" viewBox="0 0 16 18"><circle cx="8" cy="5" r="4" fill="#222"/><path d="M1 17c0-5 3-7 7-7s7 2 7 7z" fill="#222"/></svg>
      </span>
      <span class="tool" style="left:925px">
        <svg width="15" height="18" viewBox="0 0 15 18"><path d="M7.5 2c3 0 4.5 2 4.5 5v4l2 3H1l2-3V7c0-3 1.5-5 4.5-5z" fill="#222"/><circle cx="7.5" cy="15.5" r="1.8" fill="#222"/></svg>
        <span class="count" style="background:var(--dot-orange)">3</span>
      </span>
      <span class="tool" style="left:958px">
        <svg width="17" height="16" viewBox="0 0 17 16"><rect x="0.5" y="3" width="16" height="12" fill="#222"/><path d="M1 4l7.5 6L16 4" stroke="#fff" stroke-width="1.3" fill="none"/></svg>
        <span class="count" style="background:var(--dot-red)">3</span>
      </span>
      <span class="tool" style="left:996px">
        <svg width="19" height="16" viewBox="0 0 19 16"><rect y="0" width="19" height="3" fill="#111"/><rect y="6.5" width="19" height="3" fill="#111"/><rect y="13" width="19" height="3" fill="#111"/></svg>
      </span>
    </div>

    <div class="header-divider"></div>
    <div class="avatar" role="img" aria-label="User profile photo"></div>
    <div class="user">
      <div class="user-name">Lorem ipsum</div>
      <div class="user-role">HR Admin</div>
    </div>
  </header>

  <aside class="sidebar">
    <div class="search">
      <div class="search-field">
        <span>Search</span>
        <svg width="13" height="13" viewBox="0 0 13 13"><circle cx="5.5" cy="5.5" r="4.2" stroke="#fff" stroke-width="2" fill="none"/><path d="M8.5 8.5l3.5 3.5" stroke="#fff" stroke-width="2.2"/></svg>
      </div>
    </div>

    <ul class="nav-group modules">
      <li class="nav-item active">
        <span class="nav-icon"><svg width="13" height="14" viewBox="0 0 13 14"><path d="M6.5 1c2.5 0 3.8 1.8 3.8 4.2v3.3l1.7 2.5H1l1.7-2.5V5.2C2.7 2.8 4 1 6.5 1z" fill="#fff"/><circle cx="6.5" cy="12.3" r="1.4" fill="#fff"/></svg></span>
        Reminders
      </li>
      <li class="nav-item">
        <span class="nav-icon"><svg width="13" height="15" viewBox="0 0 13 15"><rect x="0.5" y="0.5" width="12" height="14" rx="1" fill="#333"/><rect x="2.5" y="2.5" width="8" height="3" fill="#fff"/><g fill="#fff"><rect x="2.5" y="7" width="2" height="2"/><rect x="5.5" y="7" width="2" height="2"/><rect x="8.5" y="7" width="2" height="2"/><rect x="2.5" y="10.5" width="2" height="2"/><rect x="5.5" y="10.5" width="2" height="2"/><rect x="8.5" y="10.5" width="2" height="2"/></g></svg></span>
        Accounts
      </li>
      <li class="nav-item">
        <span class="nav-icon"><svg width="15" height="13" viewBox="0 0 15 13"><rect x="0.5" y="2.5" width="14" height="10" rx="1.5" fill="#333"/><rect x="5" y="0.5" width="5" height="3" fill="none" stroke="#333"/><path d="M6.3 5h2.4v1.9h1.9v2.4H8.7v1.9H6.3V9.3H4.4V6.9h1.9z" fill="#fff"/></svg></span>
        Patient Requests
      </li>
      <li class="nav-item">
        <span class="nav-icon"><svg width="12" height="15" viewBox="0 0 12 15"><path d="M0.5 0.5h7.5l3.5 3.5v10.5h-11z" fill="#333"/><g fill="#fff"><rect x="2.5" y="6" width="7" height="1.2"/><rect x="2.5" y="8.5" width="7" height="1.2"/><rect x="2.5" y="11" width="7" height="1.2"/></g></svg></span>
        Reports
      </li>
      <li class="nav-item">
        <span class="nav-icon"><svg width="15" height="13" viewBox="0 0 15 13"><rect x="0.5" y="3" width="14" height="9.5" rx="1.5" fill="#333"/><rect x="5" y="0.8" width="5" height="3" fill="none" stroke="#333" stroke-width="1.4"/><rect x="0.5" y="6.5" width="14" height="1" fill="#fff"/></svg></span>
        My Company
      </li>
    </ul>

    <ul class="nav-group admin">
      <li class="nav-item">
        <span class="nav-icon"><svg width="13" height="15" viewBox="0 0 13 15"><rect x="0.5" y="0.5" width="12" height="14" rx="1" fill="#333"/><rect x="2.5" y="2.5" width="8" height="3" fill="#fff"/><g fill="#fff"><rect x="2.5" y="7" width="2" height="2"/><rect x="5.5" y="7" width="2" height="2"/><rect x="8.5" y="7" width="2" height="2"/><rect x="2.5" y="10.5" width="2" height="2"/><rect x="5.5" y="10.5" width="2" height="2"/><rect x="8.5" y="10.5" width="2" height="2"/></g></svg></span>
        Account Management
      </li>
      <li class="nav-item">
        <span class="nav-icon"><svg width="17" height="13" viewBox="0 0 17 13"><g fill="#333"><circle cx="4" cy="4" r="2.4"/><circle cx="13" cy="4" r="2.4"/><circle cx="8.5" cy="3.2" r="2.8"/><path d="M0 12c0-3 1.7-4.5 4-4.5s4 1.5 4 4.5z"/><path d="M9 12c0-3 1.7-4.5 4-4.5s4 1.5 4 4.5z"/><path d="M4 12.5c0-3.5 2-5.5 4.5-5.5S13 9 13 12.5z"/></g></svg></span>
        Employee Management
      </li>
      <li class="nav-item">
        <span class="nav-icon"><svg width="14" height="15" viewBox="0 0 14 15"><path d="M2 1v4a3.5 3.5 0 0 0 7 0V1" fill="none" stroke="#333" stroke-width="1.6"/><path d="M5.5 8.5v2a3 3 0 0 0 6 0V8" fill="none" stroke="#333" stroke-width="1.6"/><circle cx="11.5" cy="6.5" r="1.8" fill="#333"/></svg></span>
        Care Management
      </li>
    </ul>

    <footer class="sidebar-footer">Copyright © 2017 CareLoop.<br>All Rights Reserved.</footer>
  </aside>

  <table class="reminders">
    <colgroup>
      <col style="width:139px"><col style="width:146px"><col style="width:110px"><col style="width:115px">
      <col style="width:109px"><col style="width:172px"><col style="width:145px">
    </colgroup>
    <thead>
      <tr>
        <th>Lorem ipsum</th>
        <th>Diam Nonummy<span class="sort-caret"></span></th>
        <th>Ullamcorper</th>
        <th>Aliquam Elit</th>
        <th>Aliquam Elit</th>
        <th>Diam Nonummy</th>
        <th>Laoreet dolore</th>
      </tr>
    </thead>
    <tbody>
      <tr><td><span class="status overdue">laoreet dolore</span></td><td>Dolor Sit Amet</td><td>Dolor Sit Amet</td><td>Dolor Sit Amet</td><td></td><td>Aliquam Dolor Sit Amet</td><td><a class="row-link" href="#">laoreet dolore</a></td></tr>
      <tr><td><span class="status overdue">laoreet dolore</span></td><td>Dolor Sit Amet</td><td>Dolor Sit</td><td>laoreet dolore</td><td></td><td>Aliquam Dolor Sit Amet</td><td><a class="row-link" href="#">laoreet dolore</a></td></tr>
      <tr><td><span class="status overdue">laoreet dolore</span></td><td>Dolor Sit Amet</td><td>Dolor Sit</td><td>laoreet dolore</td><td></td><td>Aliquam Dolor Sit Amet</td><td><a class="row-link" href="#">laoreet dolore</a></td></tr>
      <tr><td><span class="status overdue">laoreet dolore</span></td><td>Dolor Sit Amet</td><td>Dolor Sit</td><td>laoreet dolore</td><td></td><td>Aliquam Dolor Sit Amet</td><td><a class="row-link" href="#">laoreet dolore</a></td></tr>
      <tr><td><span class="status overdue">laoreet dolore</span></td><td>Dolor Sit Amet</td><td>Dolor Sit</td><td>laoreet dolore</td><td></td><td>Aliquam Dolor Sit Amet</td><td><a class="row-link" href="#">laoreet dolore</a></td></tr>
      <tr><td><span class="status done">laoreet dolore</span></td><td>Dolor Sit Amet</td><td>Dolor Sit</td><td>laoreet dolore</td><td>Dolor Sit Amet</td><td>Aliquam Dolor Sit Amet</td><td><a class="row-link" href="#">laoreet dolore</a></td></tr>
      <tr><td><span class="status done">laoreet dolore</span></td><td>Dolor Sit Amet</td><td>Dolor Sit</td><td>laoreet dolore</td><td>Dolor Sit Amet</td><td>Aliquam Dolor Sit Amet</td><td><a class="row-link" href="#">laoreet dolore</a></td></tr>
      <tr><td><span class="status done">laoreet dolore</span></td><td>Dolor Sit Amet</td><td>Dolor Sit</td><td>laoreet dolore</td><td>Dolor Sit Amet</td><td>Aliquam Dolor Sit Amet</td><td><a class="row-link" href="#">laoreet dolore</a></td></tr>
    </tbody>
  </table>

  <nav class="pager" aria-label="Pagination">
    <svg class="pager-arrow" viewBox="0 0 23 23"><circle cx="11.5" cy="11.5" r="10.8" fill="none" stroke="#222" stroke-width="1.1"/><path d="M13.5 6.5l-5 5 5 5z" fill="none" stroke="#222" stroke-width="1.1"/></svg>
    <span class="pager-pages"><span class="current">1</span><span>2</span><span>3</span><span>4</span></span>
    <svg class="pager-arrow" viewBox="0 0 23 23"><circle cx="11.5" cy="11.5" r="10.8" fill="none" stroke="#222" stroke-width="1.1"/><path d="M9.5 6.5l5 5-5 5z" fill="none" stroke="#222" stroke-width="1.1"/></svg>
  </nav>
</body>
</html>
```